Sunny Paths and joy Business card

I have a logo, but will like a business card design. Is for a travel agency in Mexico. We focus in family experiences.

I will liek some thing different and unique, from the traditional business card, something to get remmeber for.

Business card information:

Leandro T. Ocampo
leandro@sunnypathsjoy.example

Alameda 482, 3 piso
Col. Tlalpizco
Mexico, D.F. 07320

office: (55) 5000-0142
mobile: (55) 9000-0187

www.sunnypathsjoy.example
@sunnypjoy
blog: sunnypathsandjoy.blogsite.example
facebook: SunnyPathsAndJoy

```html
<!DOCTYPE html>
<html lang="es">
<head>
<meta charset="utf-8">
<title>Sunny Paths and joy – Business card</title>
<link href="https://fonts.googleapis.com/css2?family=Exo+2:wght@400;600;700&display=swap" rel="stylesheet">
<style>
  :root {
    --brand-blue: #0b62b8;
    --logo-blue: #1f5a96;
    --logo-sky: #cfe3f3;
    --ink: #1a1a1a;
    --paper: #ffffff;
    --backdrop: #e6e6e6;
  }
  * { margin: 0; padding: 0; box-sizing: border-box; }
  html, body { width: 1200px; height: 900px; overflow: hidden; }
  body {
    background: var(--backdrop);
    font-family: "Exo 2", sans-serif;
    position: relative;
  }
  .card {
    position: absolute;
    background: var(--paper);
    overflow: hidden;
  }

  /* Front side */
  .card-front { left: 60px; top: 50px; width: 640px; height: 380px; }
  .front-stripe {
    position: absolute; left: 0; top: 150px; bottom: 0; width: 14px;
    background: var(--brand-blue);
  }
  .holder-name {
    position: absolute; left: 345px; top: 78px;
    font-size: 19px; font-weight: 600; color: var(--ink);
  }
  .address-panel {
    position: absolute; left: 355px; right: 0; top: 118px; height: 158px;
    background: var(--brand-blue); color: var(--paper);
    text-align: right; padding: 18px 22px 0 0;
    font-size: 16px; line-height: 20px;
  }
  .address-panel .phones { margin-top: 20px; }
  .online-list {
    position: absolute; right: 22px; top: 290px;
    text-align: right; font-size: 15px; line-height: 18px; color: var(--ink);
  }
  .brand-mark {
    position: absolute; left: 50px; top: 130px; width: 280px; height: 210px;
    display: flex; flex-direction: column; align-items: center; justify-content: center; gap: 14px;
  }
  .brand-mark .dot {
    width: 90px; height: 90px; border-radius: 50%; background: var(--logo-sky);
  }
  .brand-name {
    font-size: 30px; font-weight: 700; color: var(--logo-blue);
    text-align: center; line-height: 1.05;
  }

  /* Back side */
  .card-back { left: 500px; top: 470px; width: 650px; height: 380px; }
  .back-band {
    position: absolute; right: 0; top: 0; bottom: 0; width: 172px;
    background: var(--brand-blue);
  }
  .back-brand {
    position: absolute; left: 0; width: 478px; top: 50px; height: 240px;
    display: flex; flex-direction: column; align-items: center; justify-content: center; gap: 18px;
  }
  .back-brand .dot {
    width: 120px; height: 120px; border-radius: 50%; background: var(--logo-sky);
  }
  .back-brand .brand-name { font-size: 40px; }
  .back-url {
    position: absolute; left: 0; width: 478px; top: 318px;
    text-align: center; font-size: 24px; font-weight: 600; color: var(--brand-blue);
  }
</style>
</head>
<body>

<section class="card card-front" aria-label="Business card, front">
  <div class="front-stripe"></div>
  <div class="brand-mark">
    <span class="dot"></span>
    <p class="brand-name">Sunny Paths<br>and joy</p>
  </div>
  <p class="holder-name">Leandro T. Ocampo</p>
  <div class="address-panel">
    <p>Alameda 482, 3 piso</p>
    <p>Col. Tlalpizco</p>
    <p>Mexico, D.F. 07320</p>
    <div class="phones">
      <p>office: (55) 5000-0142</p>
      <p>mobile: (55) 9000-0187</p>
    </div>
  </div>
  <div class="online-list">
    <p>leandro@sunnypathsjoy.example</p>
    <p>www.sunnypathsjoy.example</p>
    <p>@sunnypjoy</p>
    <p>blog: sunnypathsandjoy.blogsite.example</p>
    <p>facebook: SunnyPathsAndJoy</p>
  </div>
</section>

<section class="card card-back" aria-label="Business card, back">
  <div class="back-brand">
    <span class="dot"></span>
    <p class="brand-name">Sunny Paths<br>and joy</p>
  </div>
  <p class="back-url">www.sunnypathsjoy.example</p>
  <div class="back-band"></div>
</section>

</body>
</html>
```